Brightpath Holdings Business Card

Create a two sided, high gloss, quality business card for Brightpath Holdings.

Target Market(s)

People wanting to purchase, scale, and sell businesses.

Industry/Entity Type

Entrepreneurs

Contact Information for Business Card

One line: Dana Corwell, CPA, CMA Another line: Entrepreneur & Investor Another line: Business Ownership Transition Expert Another line: Multi-State Licensed Real Estate Broker Phone 954-BRTPATH (278-7284) Email Dana@Brightpath Holdings.com Website www.Brightpath.com

Requirements
Must have
• Black Card, logo on one side, all other information on the other side including a small logo.
Nice to have
• Possibly add a tagline "Helping entrepreneurs live a life they don't need a vacation from"
Should not have
• There will not be a mailing address on these cards.

```html
<!DOCTYPE html>
<html lang="en">
<head>
<meta charset="UTF-8">
<title>Brightpath Holdings Business Card</title>
<link href="https://fonts.googleapis.com/css2?family=Open+Sans:wght@400;700&family=Playfair+Display:wght@400&display=swap" rel="stylesheet">
<style>
  :root {
    --backdrop: #999999;
    --card-navy: #1b212a;
    --gold: #c9a44a;
    --text-white: #ffffff;
    --text-muted: #6d7380;
    --photo-light: #ffffff;
    --photo-warm: #efe6cf;
    --photo-yellow: #d8b54a;
    --photo-blazer: #262c38;
  }
  * { margin: 0; padding: 0; box-sizing: border-box; }
  html, body {
    width: 1200px;
    height: 1200px;
    overflow: hidden;
    background: var(--backdrop);
  }
  .canvas {
    position: relative;
    width: 1200px;
    height: 1200px;
  }
  .card {
    position: absolute;
    width: 798px;
    height: 465px;
    border-radius: 25px;
    background: var(--card-navy);
    overflow: hidden;
  }
  .card-front { left: 189px; top: 91px; }
  .card-back { left: 191px; top: 605px; }

  .brand-mark {
    position: absolute;
    inset: 0;
    display: flex;
    align-items: center;
    justify-content: center;
    gap: 16px;
    padding-bottom: 12px;
  }
  .brand-dot {
    width: 30px;
    height: 30px;
    border-radius: 50%;
    background: var(--gold);
    flex: none;
  }
  .brand-name {
    font-family: "Open Sans", sans-serif;
    font-weight: 700;
    font-size: 44px;
    color: var(--gold);
    white-space: nowrap;
  }

  .info-panel {
    position: absolute;
    left: 0;
    top: 0;
    width: 410px;
    height: 100%;
  }
  .info-block {
    position: absolute;
    right: 37px;
    top: 140px;
    text-align: right;
  }
  .person-name {
    font-family: "Playfair Display", serif;
    font-weight: 400;
    font-size: 54px;
    line-height: 1.1;
    color: var(--gold);
    white-space: nowrap;
  }
  .credentials {
    margin-top: 14px;
    font-family: "Open Sans", sans-serif;
    font-size: 14px;
    line-height: 17.5px;
    color: var(--text-muted);
    white-space: nowrap;
  }
  .contact {
    margin-top: 20px;
    font-family: "Open Sans", sans-serif;
    font-size: 17.5px;
    line-height: 21.5px;
    color: var(--text-white);
    white-space: nowrap;
  }
  .small-brand {
    position: absolute;
    right: 37px;
    top: 380px;
    display: flex;
    align-items: center;
    gap: 8px;
  }
  .small-brand .brand-dot { width: 14px; height: 14px; }
  .small-brand .brand-name { font-size: 22px; }

  .portrait {
    position: absolute;
    left: 410px;
    top: 0;
    width: 388px;
    height: 100%;
    background:
      radial-gradient(ellipse 55% 70% at 48% 78%, var(--photo-yellow) 0%, rgba(216,181,74,0) 70%),
      linear-gradient(180deg, var(--photo-light) 0%, var(--photo-warm) 38%, #8f7a55 62%, var(--photo-blazer) 100%);
  }
</style>
</head>
<body>
  <div class="canvas">
    <section class="card card-front">
      <div class="brand-mark">
        <span class="brand-dot"></span>
        <span class="brand-name">Brightpath Holdings</span>
      </div>
    </section>

    <section class="card card-back">
      <div class="info-panel">
        <div class="info-block">
          <h1 class="person-name">Dana Corwell</h1>
          <p class="credentials">
            CPA, CMA, Entrepreneur, Investor,<br>
            Business Ownership Transition Expert,<br>
            Multi-State Licensed Real Estate Broker
          </p>
          <p class="contact">
            Dana@Brightpath Holdings.com<br>
            701-555-0142<br>
            Brightpath.com
          </p>
        </div>
        <div class="small-brand">
          <span class="brand-dot"></span>
          <span class="brand-name">Brightpath</span>
        </div>
      </div>
      <div class="portrait" role="img" aria-label="Portrait photograph of Dana Corwell in a dark blazer and yellow blouse, arms crossed, on a white background"></div>
    </section>
  </div>
</body>
</html>
```